Webdesign für Seminaranbieter
Zielgruppe
Die Velunor Academy bietet Kurse, Seminare & Coachings im Bereich der Kommunikation / Persönlichkeitsentwicklung an.
Folgendes Angebot besteht zur Zeit:
Seminare:
- 'Brückenbau Grundkurs Praxis', eine Einführung in die Kommunikation.
- 'Starke Wurzeln, offene Herzen' zum Thema Erziehung.
- 'Reife Jahre mit Gelassenheit', zum Thema Älter werden und den Umgang damit.
Kurse:
- 'Gewaltfreie Kommunikation', Übungsgruppe
Coaching:
- Einzelsitzungen mit Hypnose
Ps: im Anhang unter 'Angabot_Vorlage.pdf' finden Sie mehr Infos zu den einezlenen Angebote.
Aufgabenstellung
Bitte berücksichtigen Sie, dass bereits ein Logo besteht (siehe Anhang).
Vom gesamteindruck her sollte die Website aufgeräumt, übersichtlich, harmonisch, freundlich & frisch wirken.
Es wäre super, wenn die Website authentisch wirkt (und weniger '0815 Business Website').
Bitte bedenken Sie, dass die Website sich an Private richtet, die sich nach einem 'strahlenderen & unbeschwerterem Lebene sehnen'.
Wir haben bereits viele Persönlichkeiten stärken können und möchten dies auch witerhin mit viel Herzblut machen.

```html
<!DOCTYPE html>
<html lang="de">
<head>
<meta charset="utf-8">
<title>Velunor Academy</title>
<link href="https://fonts.googleapis.com/css2?family=Raleway:wght@400;500;600&display=swap" rel="stylesheet">
<style>
:root{
  --canvas:#ede7e1;
  --white:#ffffff;
  --ink:#2b2b2b;
  --muted:#555;
  --accent:#f26a44;
  --band:#f0bb87;
  --heading:#5e5270;
  --card:#f4f0eb;
  --footer:#9b8777;
  --line:#bdb6b0;
}
*{margin:0;padding:0;box-sizing:border-box}
html,body{width:1200px;height:2945px;overflow:hidden}
body{background:var(--canvas);font-family:"Raleway",sans-serif;color:var(--ink);position:relative}
.abs{position:absolute}
.page{left:135px;top:142px;width:938px;height:2718px;background:var(--white)}
.nav{left:135px;top:142px;width:938px;height:59px;background:#f6f2ee}
.brand{left:168px;top:164px;font-size:12px;letter-spacing:2px;font-weight:500}
.menu{top:168px;font-size:12px;letter-spacing:.5px;font-weight:500}
.menu-active{left:954px;top:163px;width:80px;height:22px;border:1.5px solid var(--accent);color:var(--accent);font-size:12px;text-align:center;line-height:19px;border-radius:3px}
.hero{left:135px;top:201px;width:938px;height:489px;
  background:
    radial-gradient(ellipse 45% 40% at 78% 62%,rgba(214,120,60,.55),rgba(214,120,60,0) 70%),
    radial-gradient(ellipse 35% 30% at 60% 22%,rgba(255,236,200,.85),rgba(255,236,200,0) 70%),
    radial-gradient(ellipse 40% 22% at 18% 62%,rgba(150,180,196,.9),rgba(150,180,196,0) 75%),
    radial-gradient(ellipse 70% 35% at 65% 100%,rgba(92,52,34,.95),rgba(92,52,34,0) 75%),
    linear-gradient(180deg,#c4a585 0%,#e6cba3 28%,#dcc0a0 42%,#a9b2b0 56%,#8f8a7c 72%,#6b4a35 100%)}
.hero-title{left:135px;width:938px;text-align:center;color:var(--white);text-shadow:0 1px 6px rgba(80,50,30,.35)}
.hero-name{top:476px;font-size:41px;letter-spacing:5px;font-weight:400}
.hero-tag{top:537px;font-size:19px;letter-spacing:1.5px;font-weight:500}
.dot{top:668px;width:8px;height:8px;border:1px solid #fff;border-radius:50%}
.news{left:135px;top:708px;width:938px;height:62px;background:var(--band)}
.news-label{left:272px;top:734px;font-size:11px;color:var(--white);font-weight:600;letter-spacing:.3px}
.news-input{left:541px;top:724px;width:330px;height:31px;background:var(--white);border:1px solid #ddd;font-size:11px;color:#999;letter-spacing:1.5px;padding:9px 12px}
.news-ok{left:885px;top:727px;width:40px;height:26px;background:var(--accent);color:#fff;font-size:11px;text-align:center;line-height:26px;letter-spacing:1px}
.h2{font-size:26px;letter-spacing:1.5px;color:var(--heading);font-weight:500}
.about-photo{left:288px;top:930px;width:277px;height:239px;
  background:
    radial-gradient(ellipse 30% 40% at 42% 40%,rgba(226,196,170,.95),rgba(226,196,170,0) 70%),
    radial-gradient(ellipse 45% 30% at 50% 95%,rgba(140,168,170,.95),rgba(140,168,170,0) 75%),
    radial-gradient(ellipse 30% 50% at 40% 35%,rgba(196,164,120,.7),rgba(196,164,120,0) 80%),
    linear-gradient(110deg,#b8b4ad 0%,#d9d6d0 35%,#c8ccca 65%,#9aa7a8 100%)}
.about-text{left:621px;top:928px;width:340px;font-size:14px;line-height:13.5px;color:var(--ink)}
.about-text p{margin-bottom:20px}
.quote-band{left:135px;top:1276px;width:938px;height:179px;
  background:
    radial-gradient(ellipse 40% 30% at 80% 20%,rgba(255,236,214,.8),rgba(255,236,214,0) 70%),
    radial-gradient(ellipse 50% 25% at 45% 55%,rgba(120,146,172,.7),rgba(120,146,172,0) 75%),
    radial-gradient(ellipse 40% 25% at 20% 80%,rgba(110,138,166,.8),rgba(110,138,166,0) 75%),
    radial-gradient(ellipse 12% 35% at 22% 100%,rgba(40,38,40,.9),rgba(40,38,40,0) 70%),
    linear-gradient(180deg,#ece5dc 0%,#c9d2d9 30%,#a5b7c8 60%,#91a6bb 100%)}
.card{background:var(--card);text-align:center}
.avatar{width:128px;height:128px;border-radius:50%;
  background:
    radial-gradient(circle at 45% 42%,rgba(228,198,170,.95) 0,rgba(228,198,170,0) 30%),
    radial-gradient(ellipse 60% 30% at 50% 95%,rgba(140,168,170,.95),rgba(140,168,170,0) 75%),
    linear-gradient(120deg,#c9c6c0,#dedad4 45%,#9eabae);margin:0 auto}
.quote{font-size:10.5px;line-height:13.5px;color:var(--muted);padding:0 30px}
.quote p{margin-bottom:13px}
.who{font-size:10px;font-weight:600;letter-spacing:1px;color:var(--ink)}
.where{font-size:10px;color:var(--ink)}
.scene{left:135px;top:2170px;width:938px;height:261px;
  background:
    radial-gradient(ellipse 20% 40% at 73% 40%,rgba(255,250,238,.95),rgba(255,250,238,0) 70%),
    radial-gradient(ellipse 45% 35% at 82% 95%,rgba(36,32,30,.98),rgba(36,32,30,0) 75%),
    radial-gradient(ellipse 55% 25% at 30% 88%,rgba(140,128,116,.8),rgba(140,128,116,0) 75%),
    linear-gradient(180deg,#cfd1d4 0%,#e6e5e3 40%,#cbc6c0 62%,#8d857d 82%,#4a4441 100%)}
.foot-brand{left:220px;top:2540px;width:230px;text-align:center;font-size:16px;letter-spacing:3px}
.foot-info{left:220px;width:230px;text-align:center;font-size:14px;line-height:16px}
.form-title{left:624px;top:2461px;font-size:14px;letter-spacing:1px;line-height:16px}
.field{left:624px;width:329px;border:1.5px solid var(--line);font-size:11px;letter-spacing:1.5px;color:#888;padding:9px 14px}
.send{left:626px;top:2712px;width:170px;height:31px;background:var(--accent);color:#fff;font-size:12px;letter-spacing:1.5px;text-align:center;line-height:31px;font-weight:600}
.bar{left:135px;top:2781px;width:938px;height:79px;background:var(--footer)}
.bar-link{top:2815px;font-size:13.5px;color:var(--white);letter-spacing:.5px}
</style>
</head>
<body>
<div class="abs page"></div>

<header class="abs nav"></header>
<div class="abs brand">VELUNOR ACADEMY</div>
<div class="abs menu" style="left:708px">HOME</div>
<div class="abs menu" style="left:786px">ANGEBOT</div>
<div class="abs menu" style="left:876px">KONTAKT</div>
<div class="abs menu-active">ÜBER UNS</div>

<div class="abs hero" role="img" aria-label="Foto: Gruppe jubelnder Menschen auf einem Berggipfel über einem See im warmen Abendlicht"></div>
<svg class="abs" style="left:155px;top:400px" width="30" height="50"><polyline points="22,5 5,25 22,45" fill="none" stroke="#fff" stroke-width="1.5"/></svg>
<svg class="abs" style="left:1028px;top:400px" width="30" height="50"><polyline points="8,5 25,25 8,45" fill="none" stroke="#fff" stroke-width="1.5"/></svg>
<div class="abs hero-title hero-name">VELUNOR ACADEMY</div>
<div class="abs hero-title hero-tag">NEUE PERSPEKTIVEN · NEUE HORIZONTE</div>
<div class="abs dot" style="left:585px"></div>
<div class="abs dot" style="left:598px;background:#fff"></div>
<div class="abs dot" style="left:611px"></div>

<section class="abs news"></section>
<div class="abs news-label">ABONNIEREN SIE UNSEREN NEWSLETTER!</div>
<div class="abs news-input">E-MAIL ADRESSE</div>
<div class="abs news-ok">OK</div>

<h2 class="abs h2" style="left:549px;top:842px">ÜBER UNS</h2>
<div class="abs about-photo" role="img" aria-label="Porträtfoto einer lächelnden Frau mit blondem Haar"></div>
<div class="abs about-text">
<p>Lorem ipsum dolor sit amet, mea cu nihil<br>torquatos. Ad error civibus vivendum nec. Ant-<br>iopam praesent sea an, id nam alii facete el-<br>aboraret.</p>
<p>Urbanitas adolescens vituperatoribus vel in.<br>Lorem voluptua posidonium eu sea, esse fa-<br>bellas cu eam, cu vim tation nusquam.<br>Nostrum iudicabit vix et, tota vivendo nominati<br>has cu.</p>
<p>Lorem ipsum dolor sit amet, mea cu nihil<br>torquatos. Ad error civibus vivendum nec. Ant-<br>iopam praesent sea an, id nam alii facete el-<br>aboraret. Urbanitas adolescens vituperatoribus<br>vel in. Lorem voluptua posidonium eu sea,<br>esse fabellas cu eam.</p>
</div>

<div class="abs quote-band" role="img" aria-label="Foto: Person mit erhobenen Armen auf einem Gipfel über nebligen Berghängen"></div>
<h2 class="abs h2" style="left:437px;top:1353px">DAS MEINEN UNSERE KUNDEN</h2>

<svg class="abs" style="left:178px;top:1755px" width="30" height="50"><polyline points="22,5 5,25 22,45" fill="none" stroke="#777" stroke-width="1.5"/></svg>
<svg class="abs" style="left:1008px;top:1755px" width="30" height="50"><polyline points="8,5 25,25 8,45" fill="none" stroke="#777" stroke-width="1.5"/></svg>

<div class="abs card" style="left:246px;top:1650px;width:220px;height:415px">
  <div class="avatar" role="img" aria-label="Porträtfoto der Kundin" style="margin-top:41px"></div>
  <div class="quote" style="margin-top:32px"><p>„Lorem ipsum dolor sit amet, mea cu nihil torquatos. Ad error civibus vivendum nec. Antiopam praesent sea an, id nam alii facete elaboraret.</p><p>Urbanitas adolescens vituperatoribus vel in. Lorem voluptua posidonium eu sea, esse fabellas cu eam, cu vim tation nusquam.“</p></div>
  <div class="who" style="margin-top:18px">LEA SOMMER</div><div class="where">Bergdorf</div>
</div>
<div class="abs card" style="left:498px;top:1552px;width:219px;height:414px">
  <div class="avatar" role="img" aria-label="Porträtfoto der Kundin" style="margin-top:33px"></div>
  <div class="quote" style="margin-top:28px"><p>„Lorem ipsum dolor sit amet, mea cu nihil torquatos. Ad error civibus vivendum nec. Antiopam praesent sea an, id nam alii facete elaboraret.</p><p>Urbanitas adolescens vituperatoribus vel in. ation nusquam.“</p></div>
  <div class="who" style="margin-top:52px">LEA SOMMER</div><div class="where">Bergdorf</div>
</div>
<div class="abs card" style="left:750px;top:1650px;width:220px;height:415px">
  <div class="avatar" role="img" aria-label="Porträtfoto der Kundin" style="margin-top:41px"></div>
  <div class="quote" style="margin-top:32px"><p>„Lorem ipsum dolor sit amet, mea cu nihil torquatos. Ad error civibus vivendum nec. Antiopam praesent sea an, id nam alii facete elaboraret.</p><p>Urbanitas adolescens vituperatoribus vel in. ation nusquam. Lorem ipsum dolor sit amet, mea cu nihil torqua“</p></div>
  <div class="who" style="margin-top:32px">LEA SOMMER</div><div class="where">Bergdorf</div>
</div>

<div class="abs scene" role="img" aria-label="Foto: Person sitzt auf einem Felsvorsprung über einem dunstigen Bergtal im Gegenlicht"></div>

<div class="abs foot-brand">VELUNOR ACADEMY</div>
<div class="abs foot-info" style="top:2603px;font-weight:500;letter-spacing:.5px">VELUNOR ACADEMY GMBH.</div>
<div class="abs foot-info" style="top:2635px">Lindenweg 24<br>8400 Talheim</div>
<div class="abs foot-info" style="top:2683px">TEL: 0176 987 210<br>info@velunoracademy.ch</div>

<div class="abs form-title">NOCH FRAGEN, ANREGUNGEN?<br>SCHREIBEN SIE UNS!</div>
<div class="abs field" style="top:2508px;height:33px">NAME</div>
<div class="abs field" style="top:2553px;height:33px">E-MAIL ADRESSE</div>
<div class="abs field" style="top:2595px;height:103px">NACHRICHT</div>
<div class="abs send">SENDEN</div>

<footer class="abs bar"></footer>
<div class="abs bar-link" style="left:192px">Datenschutz</div>
<div class="abs bar-link" style="left:312px">Impressum</div>
<div class="abs bar-link" style="left:533px">VELUNOR ACADEMY | 2019</div>
</body>
</html>
```